brivox new business card design project

we need a new business card design. you can view info about us @ brivox.com. i have attached an example of our previous card with our previous name that we no longer use. We really liked the design, colors etc. look below to see more info about this project. it asks for a limited number of words. please see our website for more info about our compnay.

Target Market(s)

law enforcement

Contact Information for Business Card

i have uploaded an example of what we used before that we liked.

Font styles to use
Serif

```html
<!DOCTYPE html>
<html lang="en">
<head>
<meta charset="utf-8">
<title>Brivox Business Card</title>
<link href="https://fonts.googleapis.com/css2?family=Source+Serif+4:wght@300;400;700&display=swap" rel="stylesheet">
<style>
  :root {
    --stage: #2b2b2b;
    --card-black: #1f1e1f;
    --card-blue: #10558a;
    --ink-white: #ffffff;
    --ink-soft: #e9eef3;
    --card-w: 530px;
    --card-h: 303px;
  }
  * { box-sizing: border-box; margin: 0; padding: 0; }
  html, body {
    width: 1200px;
    height: 768px;
    overflow: hidden;
    background: var(--stage);
    font-family: "Source Serif 4", Georgia, serif;
  }
  .stage {
    position: relative;
    width: 1200px;
    height: 768px;
    display: flex;
    align-items: center;
    justify-content: center;
    gap: 40px;
  }
  .card {
    position: relative;
    width: var(--card-w);
    height: var(--card-h);
    overflow: hidden;
    box-shadow: 0 10px 28px rgba(0,0,0,0.45);
  }

  /* Back side */
  .card-back {
    background: var(--card-black);
    display: flex;
    align-items: center;
    justify-content: center;
  }
  .wordmark {
    font-family: "Source Serif 4", Georgia, serif;
    font-weight: 300;
    color: var(--ink-white);
    letter-spacing: 0.16em;
    line-height: 1;
  }
  .card-back .wordmark {
    font-size: 56px;
    margin-right: -0.16em;
  }

  /* Front side */
  .card-front {
    background: var(--card-black);
    display: flex;
  }
  .front-panel {
    position: relative;
    width: 84%;
    height: 100%;
    background: var(--card-blue);
    color: var(--ink-white);
    padding: 22px 24px;
  }
  .person-name {
    font-size: 17px;
    font-weight: 700;
    line-height: 1.1;
  }
  .person-title {
    font-size: 12px;
    font-weight: 400;
    color: var(--ink-soft);
    margin-top: 1px;
  }
  .contact {
    position: absolute;
    left: 24px;
    bottom: 24px;
    font-size: 12.5px;
    font-weight: 400;
    line-height: 1.3;
  }
  .address { margin-bottom: 12px; }
  .contact-list { list-style: none; }
  .contact-list li {
    display: flex;
    align-items: center;
    gap: 10px;
    height: 20px;
  }
  .contact-list svg {
    width: 13px;
    height: 13px;
    flex: none;
    stroke: var(--ink-white);
    fill: none;
    stroke-width: 1.3;
  }
  .front-strip {
    width: 16%;
    height: 100%;
    position: relative;
  }
  .front-strip .wordmark {
    position: absolute;
    left: 50%;
    top: 50%;
    font-size: 42px;
    padding-left: 0.16em;
    transform: translate(-50%, -50%) rotate(-90deg);
    white-space: nowrap;
  }
</style>
</head>
<body>
<main class="stage">
  <section class="card card-back" aria-label="Card back">
    <span class="wordmark">BRIVOX</span>
  </section>

  <section class="card card-front" aria-label="Card front">
    <div class="front-panel">
      <p class="person-name">Alex Morgan</p>
      <p class="person-title">President</p>

      <div class="contact">
        <p class="address">1420 Alder Crest Road<br>Dallas, TX 75201</p>
        <ul class="contact-list">
          <li>
            <svg viewBox="0 0 16 16" aria-hidden="true"><path d="M3 1.5h3l1.2 3.3-1.8 1.2a8 8 0 0 0 4.6 4.6l1.2-1.8 3.3 1.2v3c0 .6-.5 1-1 1A13 13 0 0 1 2 2.5c0-.5.4-1 1-1z" fill="#fff" stroke="none"/></svg>
            <span>555.210.4470</span>
          </li>
          <li>
            <svg viewBox="0 0 16 16" aria-hidden="true"><rect x="1" y="3" width="14" height="10"/><path d="M1 3l7 6 7-6"/></svg>
            <span>info@brivox.com</span>
          </li>
          <li>
            <svg viewBox="0 0 16 16" aria-hidden="true"><circle cx="8" cy="8" r="6.5"/><ellipse cx="8" cy="8" rx="3" ry="6.5"/><path d="M1.5 8h13M2.5 4.5h11M2.5 11.5h11"/></svg>
            <span>brivox.com</span>
          </li>
        </ul>
      </div>
    </div>
    <div class="front-strip">
      <span class="wordmark">BRIVOX</span>
    </div>
  </section>
</main>
</body>
</html>
```